Präsentationsvorlagen
Zielgruppe
Die velora systems GmbH ist ein kleines Beratungsunternehmen mit drei Beratern, das sich auf Brightwell 365-Beratung spezialisiert hat. Das Unternehmen bietet Dienstleistungen in den Bereichen Security, Compliance und Device Management an, insbesondere mit Brightwell Keystra.
Darüber hinaus entwickelt velora systems das SaaS-Produkt 'Tandemo', das überprüft, ob ein B365-Tenant sicher konfiguriert ist. Tandemo basiert auf eigenen Best Practices und wird durch ein Rechtsgutachten ergänzt, um die Sicherheit eines Tenants auch aus juristischer Sicht zu bewerten.
Zielgruppe von velora systems
IT-Leiter und IT-Administratoren, die für Brightwell 365 und Security verantwortlich sind
Unternehmen, die Brightwell Keystra für ihre Geräteverwaltung einsetzen oder dies planen
IT-Dienstleister, die Security- und Compliance-Anforderungen für ihre Kunden umsetzen müssen
Krankenkassen und andere regulierte Branchen, die eine sichere und gesetzeskonforme B365-Umgebung benötigen
Aufgabenstellung
1. General Design & Functional Principles
1.1 Corporate Identity (CI) Integration
All templates must use the company’s branding (colors, fonts, logos, spacing).
Ensure that SmartArt, shapes, tables, and lists automatically adopt the branded theme when newly created.
1.2 Print & PDF Export Compatibility
Templates must translate well into A4-sized PDFs and remain visually consistent in print.
Avoid distortions when exporting or printing.
1.3 Accessibility & Readability
Maintain high contrast and readable font sizes.
Alternative text must be included for all images and media.
Support for screen readers and keyboard navigation must be ensured across all templates.
1.4 AI & Pathmate Optimization
Placeholders should include AI-friendly prompts, such as:
'Summarize this section in one sentence.'
'List three key takeaways from this slide.'
'Rewrite this paragraph at a C-suite level.'
'Generate an executive summary.'
'Provide a bulleted version of this paragraph.'
Naming conventions for placeholders should follow a structured format for AI reference, e.g.:
Executive_Summary_Box
Decision_Options_Table
Key_Takeaways_List
1.5 Flexible Content Accommodation
List-based content must support short and long variants (e.g., 3-5 items, 6-10 items).
1.6 Default Theme for Newly Created Elements
Ensure that default tables, charts, SmartArt, and shapes adopt the corporate theme.
Layouts:
Title Slide (Introduction & Branding)
Sets the stage for the presentation by introducing the topic, presenter, and company.
Includes: Main title, subtitle, company logo, and optional background image.
Agenda Slide (Navigation & Structure)
Provides an overview of the key topics and sections to help the audience follow along.
Includes: A clear agenda list (short or extended), optional icons for visual appeal.
Section Header Slide (Transitions & ..

```html
<!DOCTYPE html>
<html lang="de">
<head>
<meta charset="utf-8">
<title>velora systems – Präsentationsvorlagen</title>
<link href="https://fonts.googleapis.com/css2?family=Exo+2:wght@300;400&family=Barlow+Condensed:wght@400;500&family=Inter:wght@400;500;600&display=swap" rel="stylesheet">
<style>
:root{
  --olive:#bfbd3e;
  --lime:#d6da4a;
  --slate:#5f666c;
  --mist:#9aa3a9;
  --white:#ffffff;
  --canvas:#e3e3e3;
  --display:'Exo 2',sans-serif;
  --cond:'Barlow Condensed',sans-serif;
  --body:'Inter',sans-serif;
}
*{box-sizing:border-box;margin:0;padding:0}
html,body{width:1200px;height:2395px;overflow:hidden;background:var(--canvas)}
.slide{position:absolute;width:545px;height:307px;overflow:hidden;background:var(--white);font-family:var(--body);color:var(--slate)}
.col-l{left:25px}.col-r{left:628px}
.r1{top:31px}.r2{top:367px}.r3{top:703px}.r4{top:1039px}.r5{top:1375px}.r6{top:1711px}.r7{top:2047px}
.bg-olive{background:var(--olive)}
.abs{position:absolute}
.shape{position:absolute;inset:0;width:545px;height:307px}
.brand{position:absolute;top:28px;right:44px;display:flex;align-items:center;gap:6px;font-family:var(--display);font-weight:400;font-size:13px;letter-spacing:.5px;line-height:1}
.brand .mark{width:14px;height:14px;background:currentColor;opacity:1}
.brand.on-dark{color:var(--white)}
.brand.on-light{color:var(--slate)}
.brand.on-light .mark{background:var(--olive)}
.title{position:absolute;font-family:var(--display);font-weight:300;line-height:1.02;letter-spacing:.3px}
.title.rule::after{content:"";display:block;width:145px;height:1px;background:currentColor;margin-top:8px;opacity:.8}
.bar-left{border-left:2px solid var(--slate);padding-left:10px}
.lede{position:absolute;text-align:center;font-family:var(--cond);font-size:11px;line-height:17px;color:var(--white)}
.lede span{background:var(--slate);padding:2px 8px;box-decoration-break:clone;-webkit-box-decoration-break:clone}
.footer{position:absolute;left:31px;bottom:26px;font-size:6px;color:var(--slate)}
.footer.light{color:var(--white)}
.page{position:absolute;right:0;bottom:18px;width:30px;height:18px;font-size:6px;display:flex;align-items:center;justify-content:center}
.page.dark{background:var(--slate);color:var(--white)}
.page.light{background:var(--white);color:var(--slate)}
.desc{position:absolute;font-size:6.3px;line-height:9px}
.list{list-style:none;font-family:var(--cond);font-size:9px;line-height:11.3px}
.agenda-item{position:absolute;left:250px;width:180px;height:18px;background:var(--olive);clip-path:polygon(4% 0,100% 0,96% 100%,0 100%);display:flex;justify-content:space-between;align-items:center;padding:0 22px 0 16px}
.agenda-item b{font-family:var(--cond);font-weight:400;font-size:10px;color:var(--white)}
.agenda-item i{font-style:normal;font-family:var(--cond);font-size:7.5px;letter-spacing:.5px;color:#e9ea9c}
.panel{position:absolute;background:var(--olive);padding:18px 20px;color:#e4e78a}
.stat{position:absolute;display:flex;flex-direction:column;align-items:center;justify-content:center;color:var(--white);text-align:center;font-family:var(--display)}
.stat strong{font-weight:400;line-height:1}
.stat small{font-family:var(--body);line-height:1.2}
.axis{font-size:6px;fill:var(--slate);font-family:var(--body)}
.tbl-head{position:absolute;top:76px;font-family:var(--cond);font-size:11px;color:var(--white)}
.compare{position:absolute;top:172px;width:246px;height:69px;background:var(--olive);display:flex}
.compare .swatch{width:70px;background:var(--lime)}
.compare .txt{padding:8px 18px;color:var(--white);font-size:6.5px;line-height:10px}
.compare h3{font-family:var(--cond);font-weight:400;font-size:12px;letter-spacing:.5px;margin-bottom:4px}
.tl-label{position:absolute;font-family:var(--cond);font-size:7px;color:var(--lime);text-align:center;width:80px}
.tl-date{position:absolute;top:244px;font-size:6px;color:var(--olive)}
.step-tag{position:absolute;width:148px;height:15px;background:var(--lime);color:var(--white);font-family:var(--cond);font-size:8px;letter-spacing:.5px;padding:2px 9px}
.step-box{position:absolute;width:148px;height:52px;background:var(--slate);color:var(--white);font-size:7px;line-height:10px;padding:10px 9px}
.close-row{position:absolute;left:221px;width:272px;display:flex;font-size:6.5px;border-bottom:1px solid #e2e3b2;padding-bottom:18px}
.close-row b{width:87px;font-family:var(--cond);font-weight:500;font-size:8px;color:var(--olive);letter-spacing:.3px}
.close-row span{color:var(--slate)}
</style>
</head>
<body>

<!-- 1 Title -->
<section class="slide bg-olive col-l r1" aria-label="Title slide">
  <div class="brand on-dark"><span class="mark"></span>velora systems</div>
  <h1 class="title bar-left" style="left:42px;top:86px;font-size:34px;color:var(--white);border-color:var(--slate)">Title Slide</h1>
  <p class="lede" style="left:150px;top:170px;width:270px"><span>Sets the stage for the presentation by introducing the topic, presenter, and company.</span></p>
  <p class="footer light">Presented By Presenter | velora systems</p>
</section>

<!-- 2 Agenda -->
<section class="slide col-r r1" aria-label="Agenda slide">
  <svg class="shape" viewBox="0 0 545 307"><polygon points="388,0 545,0 545,307 250,307" fill="var(--slate)"/></svg>
  <div class="brand on-dark"><span class="mark"></span>velora systems</div>
  <h2 class="title rule" style="left:31px;top:52px;font-size:22px;color:var(--slate)">Agenda<br>Slide</h2>
  <div class="agenda-item" style="top:101px"><b>Key Topic 01</b><i>PART 1</i></div>
  <div class="agenda-item" style="top:129px"><b>Key Topic 02</b><i>PART 2</i></div>
  <div class="agenda-item" style="top:158px"><b>Key Topic 03</b><i>PART 3</i></div>
  <div class="agenda-item" style="top:187px"><b>Key Topic 04</b><i>PART 4</i></div>
  <div class="agenda-item" style="top:216px"><b>Key Topic 05</b><i>PART 5</i></div>
  <p class="footer">Presented By Presenter | velora systems</p>
</section>

<!-- 3 Section header -->
<section class="slide bg-olive col-l r2" aria-label="Section header slide">
  <svg class="shape" viewBox="0 0 545 307" role="img" aria-label="Background photo: person working on a laptop with a VPN screen">
    <defs><linearGradient id="photo" x1="0" y1="0" x2="0.6" y2="1"><stop offset="0" stop-color="#a9a83a"/><stop offset=".55" stop-color="#c8c860"/><stop offset="1" stop-color="#bfbd3e"/></linearGradient></defs>
    <polygon points="0,0 402,0 210,307 0,307" fill="url(#photo)"/>
  </svg>
  <div class="brand on-dark"><span class="mark"></span>velora systems</div>
  <h1 class="title bar-left" style="left:42px;top:110px;font-size:28px;color:var(--white)">Section Header<br>Slide</h1>
  <p class="lede" style="left:165px;top:217px;width:250px"><span>Clearly marks new sections in the presentation, making content transitions smoother.</span></p>
</section>

<!-- 4 Content -->
<section class="slide col-r r2" aria-label="Content slide with two lists">
  <svg class="shape" viewBox="0 0 545 307"><polygon points="0,0 253,0 132,307 0,307" fill="var(--olive)"/></svg>
  <div class="brand on-light"><span class="mark"></span>velora systems</div>
  <h2 class="title rule" style="left:31px;top:38px;font-size:22px;color:var(--slate)">Content<br>Slide</h2>
  <p class="desc" style="left:30px;top:109px;width:132px;color:#e6e88f">Presents structured textual information in a way that is easy to read and digest. Includes: Headings, paragraphs, bullet points, numbered lists, optional icons for clarity.</p>
  <div class="panel" style="left:234px;top:142px;width:132px;height:87px"><ul class="list"><li>• Point 01</li><li>• Point 02</li><li>• Point 03</li><li>• Point 04</li><li>• Point 05</li></ul></div>
  <div class="panel" style="left:387px;top:142px;width:132px;height:87px"><ul class="list"><li>1.&nbsp; Number 01</li><li>2.&nbsp; Number 02</li><li>3.&nbsp; Number 03</li><li>4.&nbsp; Number 04</li><li>5.&nbsp; Number 05</li></ul></div>
  <p class="footer">Presented By Presenter | velora systems</p>
  <div class="page dark">4</div>
</section>

<!-- 5 Content split -->
<section class="slide bg-olive col-l r3" aria-label="Content slide with text and lists">
  <svg class="shape" viewBox="0 0 545 307"><polygon points="401,0 545,0 545,307 263,307" fill="var(--slate)"/></svg>
  <div class="brand on-dark"><span class="mark"></span>velora systems</div>
  <h2 class="title" style="left:60px;top:98px;width:182px;text-align:right;font-size:22px;color:var(--slate)">Content Slide</h2>
  <div class="abs" style="left:80px;top:127px;width:162px;height:1px;background:var(--slate)"></div>
  <p class="desc" style="left:60px;top:150px;width:182px;text-align:right;color:var(--slate)">Presents structured textual information in a way that is easy to read and digest. Includes: Headings, paragraphs, bullet points, numbered lists, optional icons for clarity.</p>
  <ul class="list abs" style="left:392px;top:102px;color:var(--white)"><li>• Point 01</li><li>• Point 02</li><li>• Point 03</li><li>• Point 04</li><li>• Point 05</li></ul>
  <ul class="list abs" style="left:392px;top:186px;color:var(--white)"><li>1.&nbsp; Number 01</li><li>2.&nbsp; Number 02</li><li>3.&nbsp; Number 03</li><li>4.&nbsp; Number 04</li><li>5.&nbsp; Number 05</li></ul>
  <p class="footer light">Presented By Presenter | velora systems</p>
  <div class="page light">5</div>
</section>

<!-- 6 Line chart -->
<section class="slide col-r r3" aria-label="Line chart slide">
  <h2 class="title rule" style="left:59px;top:38px;font-size:22px;color:var(--slate)">Line Slide</h2>
  <p class="desc" style="left:59px;top:84px;width:180px">Helps communicate data-driven insights in a visually compelling manner. Includes: Bar charts, pie charts, line graphs, and consistent formatting for clarity.</p>
  <div class="stat" style="left:267px;top:38px;width:93px;height:69px;background:var(--olive)"><strong style="font-size:26px">100</strong><small style="font-size:6.5px">readers appreciate<br>accurate information</small></div>
  <div class="stat" style="left:377px;top:38px;width:93px;height:69px;background:var(--slate)"><strong style="font-size:26px">75</strong><small style="font-size:6.5px">readers appreciate<br>accurate information</small></div>
  <svg class="shape" viewBox="0 0 545 307" aria-label="Line chart comparing two series across four data points">
    <g stroke="#d9dbdd" stroke-width=".6"><line x1="48" y1="136" x2="508" y2="136"/><line x1="48" y1="163" x2="508" y2="163"/><line x1="48" y1="190" x2="508" y2="190"/><line x1="48" y1="218" x2="508" y2="218"/></g>
    <g class="axis"><text x="30" y="138">100</text><text x="34" y="165">75</text><text x="34" y="192">50</text><text x="34" y="220">25</text><text x="38" y="247">0</text>
    <text x="38" y="256">Data 01</text><text x="191" y="256">Data 02</text><text x="344" y="256">Data 03</text><text x="497" y="256">Data 04</text></g>
    <polyline points="48,185 201,198 354,168 508,181" fill="none" stroke="var(--olive)" stroke-width="1.2"/>
    <polyline points="48,225 201,217 354,187 508,137" fill="none" stroke="var(--slate)" stroke-width="1.2"/>
    <g fill="var(--olive)"><circle cx="48" cy="185" r="1.8"/><circle cx="201" cy="198" r="1.8"/><circle cx="354" cy="168" r="1.8"/><circle cx="508" cy="181" r="1.8"/></g>
    <g fill="var(--slate)"><circle cx="48" cy="225" r="1.8"/><circle cx="201" cy="217" r="1.8"/><circle cx="354" cy="187" r="1.8"/><circle cx="508" cy="137" r="1.8"/></g>
  </svg>
  <p class="footer">Presented By Presenter | velora systems</p>
  <div class="page dark">6</div>
</section>

<!-- 7 Bar chart -->
<section class="slide col-l r4" aria-label="Bar chart slide">
  <div class="brand on-light"><span class="mark"></span>velora systems</div>
  <h2 class="title rule" style="left:33px;top:38px;font-size:22px;color:var(--slate)">Bar Slide</h2>
  <p class="desc" style="left:33px;top:84px;width:180px">Helps communicate data-driven insights in a visually compelling manner. Includes: Bar charts, pie charts, line graphs, and consistent formatting for clarity.</p>
  <div class="stat" style="left:33px;top:128px;width:90px;height:39px;background:var(--olive)"><strong style="font-size:15px">100</strong><small style="font-size:3.6px">readers appreciate accurate information</small></div>
  <div class="stat" style="left:33px;top:173px;width:90px;height:39px;background:var(--slate)"><strong style="font-size:15px">75</strong><small style="font-size:3.6px">readers appreciate accurate information</small></div>
  <div class="stat" style="left:33px;top:218px;width:90px;height:39px;background:var(--mist)"><strong style="font-size:15px">50</strong><small style="font-size:3.6px">readers appreciate accurate information</small></div>
  <svg class="shape" viewBox="0 0 545 307" aria-label="Grouped bar chart April to July">
    <text class="axis" transform="translate(158,200) rotate(-90)" font-weight="600">Werteachse</text>
    <g><rect x="186" y="237" width="18" height="30" fill="var(--olive)"/><rect x="205" y="167" width="18" height="100" fill="var(--slate)"/><rect x="224" y="177" width="18" height="90" fill="var(--mist)"/></g>
    <g><rect x="271" y="221" width="18" height="46" fill="var(--olive)"/><rect x="290" y="190" width="18" height="77" fill="var(--slate)"/><rect x="309" y="199" width="18" height="68" fill="var(--mist)"/></g>
    <g><rect x="356" y="171" width="18" height="96" fill="var(--olive)"/><rect x="375" y="140" width="18" height="127" fill="var(--slate)"/><rect x="394" y="234" width="18" height="33" fill="var(--mist)"/></g>
    <g><rect x="442" y="92" width="18" height="175" fill="var(--olive)"/><rect x="461" y="162" width="18" height="105" fill="var(--slate)"/><rect x="480" y="195" width="18" height="72" fill="var(--mist)"/></g>
    <g class="axis" font-weight="600"><text x="207" y="278">April</text><text x="293" y="278">Mai</text><text x="378" y="278">Juni</text><text x="465" y="278">Juli</text></g>
  </svg>
  <p class="footer">Presented By Presenter | velora systems</p>
  <div class="page dark">7</div>
</section>

<!-- 8 Pie chart -->
<section class="slide col-r r4" aria-label="Pie chart slide">
  <div class="brand on-light"><span class="mark"></span>velora systems</div>
  <h2 class="title rule" style="left:31px;top:104px;font-size:22px;color:var(--slate)">Pie Slide</h2>
  <p class="desc" style="left:31px;top:150px;width:180px">Helps communicate data-driven insights in a visually compelling manner. Includes: Bar charts, pie charts, line graphs, and consistent formatting for clarity.</p>
  <svg class="shape" viewBox="0 0 545 307" aria-label="Donut chart with four segments">
    <g fill="none" stroke-width="16" transform="translate(315,113)">
      <circle r="65" stroke="var(--slate)" stroke-dasharray="120 290" transform="rotate(-90)"/>
      <circle r="65" stroke="var(--olive)" stroke-dasharray="141 270" transform="rotate(19)"/>
      <circle r="65" stroke="var(--lime)" stroke-dasharray="71 340" transform="rotate(145)"/>
      <circle r="65" stroke="var(--mist)" stroke-dasharray="67 345" transform="rotate(210)"/>
    </g>
  </svg>
  <div class="stat" style="left:110px;top:218px;width:92px;height:40px;background:var(--lime)"><strong style="font-size:15px">120</strong><small style="font-size:3.6px">readers appreciate accurate information</small></div>
  <div class="stat" style="left:220px;top:218px;width:93px;height:40px;background:var(--olive)"><strong style="font-size:15px">100</strong><small style="font-size:3.6px">readers appreciate accurate information</small></div>
  <div class="stat" style="left:326px;top:218px;width:93px;height:40px;background:var(--slate)"><strong style="font-size:15px">75</strong><small style="font-size:3.6px">readers appreciate accurate information</small></div>
  <div class="stat" style="left:428px;top:218px;width:92px;height:40px;background:var(--mist)"><strong style="font-size:15px">50</strong><small style="font-size:3.6px">readers appreciate accurate information</small></div>
  <p class="footer">Presented By Presenter | velora systems</p>
  <div class="page dark">8</div>
</section>

<!-- 9 Table -->
<section class="slide col-l r5" aria-label="Table slide">
  <svg class="shape" viewBox="0 0 545 307"><polygon points="251,0 545,0 545,307 114,307" fill="var(--olive)"/></svg>
  <div class="brand on-dark"><span class="mark"></span>velora systems</div>
  <h2 class="title rule" style="left:29px;top:35px;font-size:22px;color:var(--slate)">Table Slide</h2>
  <p class="desc" style="left:29px;top:103px;width:120px">Helps communicate data-driven insights in a visually compelling manner. Includes: Bar charts, pie charts, line graphs, and consistent formatting for clarity.</p>
  <span class="tbl-head" style="left:250px">Headline</span><span class="tbl-head" style="left:320px">Headline</span><span class="tbl-head" style="left:391px">Headline</span><span class="tbl-head" style="left:461px">Headline</span>
  <svg class="shape" viewBox="0 0 545 307" aria-label="Table grid with four columns">
    <g stroke="#e8e9b8" stroke-width=".7">
      <line x1="235" y1="93" x2="515" y2="93"/><line x1="235" y1="135" x2="515" y2="135"/><line x1="235" y1="176" x2="515" y2="176"/><line x1="235" y1="218" x2="515" y2="218"/>
      <line x1="305" y1="76" x2="305" y2="258"/><line x1="375" y1="76" x2="375" y2="258"/><line x1="445" y1="76" x2="445" y2="258"/>
    </g>
  </svg>
  <p class="footer" style="color:#c8cbcd">Presented By Presenter | velora systems</p>
  <div class="page light">9</div>
</section>

<!-- 10 Comparison -->
<section class="slide col-r r5" aria-label="Comparison content slide">
  <svg class="shape" viewBox="0 0 545 307"><polygon points="0,0 85,0 0,185" fill="var(--olive)"/></svg>
  <div class="brand on-light"><span class="mark"></span>velora systems</div>
  <h2 class="title rule" style="left:95px;top:58px;font-size:22px;color:var(--slate)">Content Slide</h2>
  <p class="desc" style="left:284px;top:93px;width:220px;font-size:7px;line-height:10px">Highlights differences between options, concepts, or approaches in a structured format.<br><br>Includes: Two- or three-column layouts, equal or varied column widths, and clear labeling.</p>
  <div class="compare" style="left:28px"><div class="swatch"></div><div class="txt"><h3>Side 01</h3>Summarize the key points here.<br>&nbsp;&nbsp;• Bullet points<br>&nbsp;&nbsp;• Bullet points</div></div>
  <div class="compare" style="left:283px"><div class="swatch"></div><div class="txt"><h3>Side 02</h3>Summarize the key points here.<br>&nbsp;&nbsp;• Bullet points<br>&nbsp;&nbsp;• Bullet points</div></div>
  <p class="footer">Presented By Presenter | velora systems</p>
  <div class="page dark">10</div>
</section>

<!-- 11 Timeline -->
<section class="slide col-l r6" aria-label="Timeline slide">
  <svg class="shape" viewBox="0 0 545 307" aria-label="Timeline with seven milestones">
    <polygon points="0,0 85,0 0,175" fill="var(--olive)"/>
    <line x1="30" y1="237" x2="500" y2="237" stroke="#e6e89a" stroke-width=".8"/>
    <g fill="var(--lime)"><circle cx="57" cy="170" r="15"/><circle cx="200" cy="170" r="15"/><circle cx="193" cy="215" r="15"/><circle cx="290" cy="148" r="15"/><circle cx="320" cy="193" r="15"/><circle cx="438" cy="215" r="15"/><circle cx="497" cy="193" r="15"/></g>
  </svg>
  <div class="brand on-light"><span class="mark"></span>velora systems</div>
  <h2 class="title rule" style="left:110px;top:30px;font-size:22px;color:var(--slate)">Timeline Slide</h2>
  <p class="desc" style="left:110px;top:76px;width:190px">Helps communicate data-driven insights in a visually compelling manner. Includes: Bar charts, pie charts, line graphs, and consistent formatting for clarity.</p>
  <span class="tl-label" style="left:17px;top:145px">Sign Off</span>
  <span class="tl-label" style="left:160px;top:145px">Assign PM</span>
  <span class="tl-label" style="left:153px;top:190px">Project Approval</span>
  <span class="tl-label" style="left:250px;top:123px">Data Back-Up</span>
  <span class="tl-label" style="left:280px;top:168px">Checkpoint A</span>
  <span class="tl-label" style="left:398px;top:190px">Certification</span>
  <span class="tl-label" style="left:457px;top:168px">Checkpoint B</span>
  <span class="tl-date" style="left:30px">01/18/25</span><span class="tl-date" style="left:143px">04/12/25</span><span class="tl-date" style="left:256px">07/05/25</span><span class="tl-date" style="left:370px">09/27/25</span><span class="tl-date" style="left:484px">12/20/25</span>
  <p class="footer">Presented By Presenter | velora systems</p>
  <div class="page dark">11</div>
</section>

<!-- 12 Next steps -->
<section class="slide col-r r6" aria-label="Next steps slide">
  <svg class="shape" viewBox="0 0 545 307"><polygon points="258,0 545,0 545,307 115,307" fill="var(--olive)"/></svg>
  <h2 class="title rule" style="left:31px;top:40px;font-size:22px;color:var(--slate)">Next Steps</h2>
  <p class="desc" style="left:31px;top:86px;width:112px;font-size:6.3px">Where do you go from here? Sustainability reports are not just about looking back, but also looking forward. This SDG Progress Report is a continuous work in progress – a way for your organization to track its impact and improvements over time. This section outlines your strategy for continuing the good work done so far.</p>
  <span class="step-tag" style="left:208px;top:31px">1. Step 01</span><span class="step-tag" style="left:370px;top:31px">2. Step 02</span>
  <div class="step-box" style="left:208px;top:49px">Outlines structured processes, workflows, or step-by-step guidance.</div><div class="step-box" style="left:370px;top:49px">Outlines structured processes, workflows, or step-by-step guidance.</div>
  <span class="step-tag" style="left:208px;top:115px">3. Step 03</span><span class="step-tag" style="left:370px;top:115px">4. Step 04</span>
  <div class="step-box" style="left:208px;top:133px">Outlines structured processes, workflows, or step-by-step guidance.</div><div class="step-box" style="left:370px;top:133px">Outlines structured processes, workflows, or step-by-step guidance.</div>
  <span class="step-tag" style="left:208px;top:200px">5. Step 05</span><span class="step-tag" style="left:370px;top:200px">6. Step 06</span>
  <div class="step-box" style="left:208px;top:218px">Outlines structured processes, workflows, or step-by-step guidance.</div><div class="step-box" style="left:370px;top:218px">Outlines structured processes, workflows, or step-by-step guidance.</div>
  <p class="footer" style="color:var(--mist)">Presented By Presenter | velora systems</p>
  <div class="page light">12</div>
</section>

<!-- 13 Conclusion -->
<section class="slide col-l r7" aria-label="Conclusion and next steps slide">
  <svg class="shape" viewBox="0 0 545 307"><polygon points="0,0 238,0 100,307 0,307" fill="var(--olive)"/></svg>
  <h2 class="abs" style="left:31px;top:32px;font-family:var(--cond);font-weight:400;font-size:14px;line-height:16px;color:var(--slate)">Conclusion &amp; Next Steps Slide<br>(Closing &amp; Action Items)</h2>
  <div class="close-row" style="top:75px"><b>Step 01</b><span>next actions, contact details, or interactive Q&amp;A section.</span></div>
  <div class="close-row" style="top:117px"><b>Step 02</b><span>next actions, contact details, or interactive Q&amp;A section.</span></div>
  <div class="close-row" style="top:160px"><b>Step 03</b><span>next actions, contact details, or interactive Q&amp;A section.</span></div>
  <div class="close-row" style="top:199px"><b>Step 04</b><span>next actions, contact details, or interactive Q&amp;A section.</span></div>
  <div class="close-row" style="top:239px;border:0"><b>Step 05</b><span>next actions, contact details, or interactive Q&amp;A section.</span></div>
  <div class="page dark">13</div>
</section>

<!-- 14 Contact -->
<section class="slide bg-olive col-r r7" aria-label="Contact slide">
  <svg class="shape" viewBox="0 0 545 307"><polygon points="0,0 84,0 0,175" fill="var(--white)"/><polygon points="380,0 545,0 545,307 241,307" fill="var(--slate)"/></svg>
  <div class="brand on-dark"><span class="mark"></span>velora systems</div>
  <div class="abs" style="left:69px;top:163px;font-family:var(--cond);font-size:9px;line-height:11px;color:var(--white)">
    <p style="font-weight:500">Lindenweg 14<br>48231 Talheim am See</p>
    <p style="margin-top:12px">+49 5361 2047718</p>
    <p style="margin-top:22px">www.velorasystems.de</p>
    <p style="margin-top:6px">briefkasten@velorasystems.de</p>
  </div>
  <div class="abs" style="left:358px;top:204px;width:70px;height:1px;background:var(--white)"></div>
  <p class="desc" style="left:358px;top:213px;width:150px;color:var(--white)">Guter Rat muss nicht teuer sein. Buche hier schnell, einfach und unverbindlich ein erstes Gespräch. Wir nehmen uns Zeit und sprechen über deine Möglichkeiten.</p>
</section>

</body>
</html>
```